Learning Uplift Collective Website

Background

Learning Uplift Collective (LUC) is a newly established consultancy that focuses on education, primarily improving schools and universities. The company is registered in Dubai.

Domain name is learnuplift.com, the logo for LUC is attached as is the registered business address

Scope

LUC requests designers to design and build a website that initially includes the following key pages/sections.

• About us/our story
• Our people
• Our services
• Our work
• Contact us/social media

Some examples of websites that are similar to the look and feel of a new contemporary startup like LUC include the following:
http://www.tarvel.co/journal/
https://www.mizrenadvisory.com/

Content to be provided by LUC. In addition, LUC wishes the successful designer to set up all email and social media accounts required.

Target Market(s)

Government Education departments, donors, Private school chains, school owners, NGOs, investors

Industry/Entity Type

Education

Number of Pages Required

3 page

Font styles to use
Sans Serif

Colors

Designer to choose colors to be used in the design.

Requirements
Must have
• • About us/our story
• • Our people
• • Our services
• • Our work
• • Contact us/social media
• (Maximum 3 pages)
• domain name, address, our services etc
• Blend colours with logo design colours
Nice to have
• Given the migration to mobile devices, we think that having a site which can be scrolled from top to bottom would be preferable
• Possibly a lite version in areas where bandwidth is poor?
Should not have
• Anything that takes a long time to download

```html
<!DOCTYPE html>
<html lang="en">
<head>
<meta charset="utf-8">
<title>Learning Uplift Collective</title>
<link rel="stylesheet" href="https://fonts.googleapis.com/css2?family=Montserrat:wght@400;600;700&family=Open+Sans:wght@400;600;700&display=swap">
<style>
:root{
  --navy:#2e3d8a;
  --teal:#3ba9be;
  --text:#6b6f78;
  --dark:#333a45;
  --grey-bg:#f5f5f6;
  --line:#d6d8dc;
  --white:#ffffff;
}
*{box-sizing:border-box;margin:0;padding:0}
html,body{width:1200px;height:2880px;overflow:hidden;background:var(--white)}
body{position:relative;font-family:"Open Sans",Arial,sans-serif;color:var(--text)}
.abs{position:absolute}

/* header */
.site-header{position:absolute;left:0;top:0;width:1200px;height:117px;background:var(--white)}
.brand{position:absolute;left:77px;top:30px;display:flex;align-items:center;gap:12px}
.brand-mark{width:48px;height:48px;border-radius:50%;background:var(--navy)}
.brand-name{font-family:"Montserrat",Arial,sans-serif;font-weight:700;font-size:30px;color:var(--navy);line-height:1.05}
.main-nav{position:absolute;right:71px;top:51px;display:flex;gap:30px;font-family:"Montserrat",Arial,sans-serif;font-size:12px;font-weight:600;color:var(--dark);letter-spacing:.2px;white-space:nowrap}
.main-nav .is-active{color:var(--navy);font-weight:700}

/* hero */
.hero{position:absolute;left:0;top:117px;width:1200px;height:545px;background:linear-gradient(180deg,#7c8ea3 0%,#5f6f80 35%,#4a5563 65%,#3c4650 100%)}
.hero-title{position:absolute;left:0;width:1200px;top:185px;text-align:center;font-family:"Montserrat",Arial,sans-serif;font-weight:700;font-size:42px;line-height:44px;color:var(--white);text-transform:uppercase}
.hero-sub{position:absolute;left:0;width:1200px;top:282px;text-align:center;font-family:"Montserrat",Arial,sans-serif;font-weight:600;font-size:29px;line-height:39px;color:var(--white)}
.hero-arrow{position:absolute;top:250px}
.btn{position:absolute;display:flex;align-items:center;justify-content:center;background:var(--teal);color:var(--white);border-radius:26px;font-family:"Montserrat",Arial,sans-serif;font-weight:700;font-size:13px;letter-spacing:.3px;white-space:nowrap}

/* section labels */
.kicker{font-family:"Montserrat",Arial,sans-serif;font-weight:700;font-size:12px;color:var(--dark);letter-spacing:.4px;white-space:nowrap}
.section-title{font-family:"Montserrat",Arial,sans-serif;font-weight:700;font-size:38px;color:var(--navy);line-height:1;white-space:nowrap}
.divider-v{position:absolute;width:2px;background:var(--line)}

/* about */
.about-text{left:372px;top:745px;width:700px;font-size:13.5px;line-height:27px}
.about-countries{left:372px;top:808px;width:700px;font-size:15px;line-height:27px;color:var(--navy)}

/* services */
.services{position:absolute;left:0;top:1023px;width:1200px;height:613px;background:var(--grey-bg)}
.service-card{position:absolute;top:164px;width:328px;height:293px;background:var(--white);text-align:center}
.service-icon{position:absolute;left:108px;top:26px}
.service-name{position:absolute;left:8px;right:8px;top:166px;font-family:"Montserrat",Arial,sans-serif;font-weight:600;font-size:17px;line-height:27px;color:var(--teal);text-transform:uppercase;white-space:nowrap}
.service-name.is-compact{font-size:14px;line-height:25px;top:168px}
.service-more{position:absolute;left:0;right:0;top:242px;font-family:"Montserrat",Arial,sans-serif;font-weight:700;font-size:13px;color:var(--navy)}

/* work */
.work-photo{position:absolute;left:0;top:1636px;width:453px;height:388px;background:linear-gradient(135deg,#c9b7a6 0%,#8d7a6c 45%,#3d4250 100%)}
.work-text{left:492px;top:1709px;width:340px;font-size:13.5px;line-height:28px}

/* people */
.people{position:absolute;left:0;top:2024px;width:1200px;height:388px;background:var(--grey-bg)}
.person-photo{position:absolute;top:84px;width:150px;height:127px}
.person-name{position:absolute;top:82px;font-family:"Montserrat",Arial,sans-serif;font-weight:700;font-size:15px;color:var(--navy)}
.person-role{position:absolute;top:106px;font-size:13px;color:var(--teal)}
.person-bio{position:absolute;top:133px;width:172px;font-size:13px;line-height:23px}

/* contact */
.footer-head{font-family:"Montserrat",Arial,sans-serif;font-weight:700;font-size:15px;color:var(--navy)}
.address{left:77px;top:2519px;width:300px;font-size:13.5px;line-height:24px;color:var(--dark)}
.address .org{font-family:"Montserrat",Arial,sans-serif;font-weight:700;font-size:12.5px;color:var(--teal)}
.contact-line{position:absolute;left:77px;display:flex;align-items:center;gap:16px;font-size:13.5px;color:var(--dark)}
.field{position:absolute;height:38px;border:1px solid #c9ccd1;background:var(--white);font-size:12px;color:var(--dark);padding:10px 12px}
.field-select::after{content:"";position:absolute;right:14px;top:15px;border:4px solid transparent;border-top:5px solid var(--dark);border-bottom:none}

/* bottom bar */
.bottom-bar{position:absolute;left:0;top:2796px;width:1200px;height:84px;background:var(--grey-bg)}
.copyright{position:absolute;left:77px;top:36px;font-size:12px;color:var(--text)}
.social{position:absolute;right:80px;top:30px;display:flex;gap:20px}
.social span{width:20px;height:20px;border-radius:50%;background:#5c6270}
</style>
</head>
<body>

<header class="site-header">
  <div class="brand"><span class="brand-mark"></span><span class="brand-name">LUC</span></div>
  <nav class="main-nav">
    <span class="is-active">HOME</span>
    <span>ABOUT US/OUR STORY</span>
    <span>OUR PEOPLE</span>
    <span>OUR SERVICES</span>
    <span>OUR WORK</span>
    <span>CONTACT US</span>
  </nav>
</header>

<section class="hero" role="img" aria-label="Aerial view of a modern city skyline with towers and highway interchanges at dusk">
  <svg class="hero-arrow" style="left:60px" width="24" height="40" viewBox="0 0 24 40"><path d="M18 6 L6 20 L18 34" fill="none" stroke="#fff" stroke-width="4"/></svg>
  <svg class="hero-arrow" style="right:60px" width="24" height="40" viewBox="0 0 24 40"><path d="M6 6 L18 20 L6 34" fill="none" stroke="#fff" stroke-width="4"/></svg>
  <h1 class="hero-title">Learning Uplift<br>Collective FZC</h1>
  <p class="hero-sub">Learning Uplift Collective (LUC) is a newly<br>established consultancy in Dubai..</p>
  <a class="btn" style="left:520px;top:378px;width:160px;height:50px">READ MORE</a>
</section>

<section class="about">
  <div class="abs kicker" style="left:77px;top:815px">ABOUT US</div>
  <h2 class="abs section-title" style="left:77px;top:836px">OUR STORY</h2>
  <div class="divider-v" style="left:340px;top:716px;height:254px"></div>
  <p class="abs about-text">The Partners have extensive international educational consultancy experience and have worked extensively improving schools, universities, education systems with delivery in the following countries:</p>
  <p class="abs about-countries">United Kingdom, Australia, Germany, United States, Bahrain, U.A.E, Pakistan, India, South Africa, Saudi Arabia, Jordan.</p>
  <a class="btn" style="left:374px;top:893px;width:162px;height:48px">READ MORE</a>
</section>

<section class="services">
  <div class="abs kicker" style="left:0;width:1200px;text-align:center;top:54px">WHAT WE DO</div>
  <h2 class="abs section-title" style="left:0;width:1200px;text-align:center;top:76px">OUR SERVICES</h2>

  <div class="service-card" style="left:77px">
    <svg class="service-icon" width="112" height="112" viewBox="0 0 112 112"><circle cx="56" cy="56" r="54" fill="none" stroke="var(--navy)" stroke-width="3"/><path d="M32 50 L56 40 L80 50 L56 60 Z" fill="var(--teal)"/><path d="M42 55 V66 Q56 74 70 66 V55 L56 61 Z" fill="var(--teal)"/><path d="M76 52 V66" stroke="var(--teal)" stroke-width="2.5"/></svg>
    <div class="service-name">Learning Uplift<br>Collective Design</div>
    <div class="service-more">Read More</div>
  </div>
  <div class="service-card" style="left:438px">
    <svg class="service-icon" width="112" height="112" viewBox="0 0 112 112"><circle cx="56" cy="56" r="54" fill="none" stroke="var(--navy)" stroke-width="3"/><path d="M34 44 L56 32 L78 44 Z" fill="var(--teal)"/><rect x="36" y="46" width="40" height="4" fill="var(--teal)"/><rect x="40" y="52" width="5" height="18" fill="var(--teal)"/><rect x="50" y="52" width="5" height="18" fill="var(--teal)"/><rect x="60" y="52" width="5" height="18" fill="var(--teal)"/><rect x="69" y="52" width="5" height="18" fill="var(--teal)"/><rect x="34" y="72" width="44" height="5" fill="var(--teal)"/></svg>
    <div class="service-name is-compact">Deliver &amp; Support Government<br>Education Systems</div>
    <div class="service-more">Read More</div>
  </div>
  <div class="service-card" style="left:795px">
    <svg class="service-icon" width="112" height="112" viewBox="0 0 112 112"><circle cx="56" cy="56" r="54" fill="none" stroke="var(--navy)" stroke-width="3"/><rect x="46" y="38" width="20" height="38" fill="var(--teal)"/><rect x="32" y="50" width="14" height="26" fill="var(--teal)"/><rect x="66" y="50" width="14" height="26" fill="var(--teal)"/><path d="M56 28 V38" stroke="var(--teal)" stroke-width="2"/><path d="M56 28 H63 V32 H56" fill="var(--teal)"/><rect x="52" y="64" width="8" height="12" fill="#fff"/><rect x="50" y="44" width="4" height="4" fill="#fff"/><rect x="58" y="44" width="4" height="4" fill="#fff"/><rect x="36" y="56" width="4" height="4" fill="#fff"/><rect x="72" y="56" width="4" height="4" fill="#fff"/></svg>
    <div class="service-name">Public and Private<br>Universities</div>
    <div class="service-more">Read More</div>
  </div>

  <a class="btn" style="left:501px;top:511px;width:198px;height:48px">VIEW ALL SERVICES</a>
</section>

<section class="work">
  <div class="work-photo" role="img" aria-label="Two colleagues reviewing work together on a tablet at a desk"></div>
  <p class="abs work-text">Aliquam molestie, mi et imperdiet euismod, dui purus auctor tellus, et interdum lacus lectus et ante. Sed accumsan sollicitudin sapien, sit amet adipiscing turpis gravida ac. In congue, neque ac lobortis volutpat, libero mauris varius mi, vitae suscipit ipsum ligula vitae risus.</p>
  <a class="btn" style="left:492px;top:1897px;width:161px;height:48px">READ MORE</a>
  <div class="divider-v" style="left:856px;top:1701px;height:255px"></div>
  <div class="abs kicker" style="right:73px;top:1799px">WHAT WE DONE</div>
  <h2 class="abs section-title" style="right:73px;top:1820px">OUR WORK</h2>
</section>

<section class="people">
  <div class="abs kicker" style="left:77px;top:163px">OUR TEAM</div>
  <h2 class="abs section-title" style="left:77px;top:185px;font-size:34px">OUR PEOPLE</h2>
  <div class="divider-v" style="left:340px;top:65px;height:255px"></div>

  <div class="person-photo" style="left:374px;background:linear-gradient(160deg,#a9b4bf,#6d7888)" role="img" aria-label="Portrait of a partner in a grey sweater"></div>
  <div class="person-name" style="left:555px">NAME HEADING</div>
  <div class="person-role" style="left:555px">( Partners )</div>
  <p class="person-bio" style="left:555px">Vestibulum ante ipsum primis in faucibus orci luctus et ultrices posuere cubilia lobortis turpis..</p>
  <a class="btn" style="left:555px;top:255px;width:159px;height:48px">READ MORE</a>

  <div class="person-photo" style="left:774px;background:linear-gradient(160deg,#c9a98e,#7d6a5c)" role="img" aria-label="Portrait of a partner in a checked shirt"></div>
  <div class="person-name" style="left:954px">NAME HEADING</div>
  <div class="person-role" style="left:954px">( Partners )</div>
  <p class="person-bio" style="left:954px">Vestibulum ante ipsum primis in faucibus orci luctus et ultrices posuere cubilia lobortis turpis..</p>
  <a class="btn" style="left:954px;top:255px;width:160px;height:48px">READ MORE</a>
</section>

<section class="contact">
  <div class="abs footer-head" style="left:77px;top:2487px">ADDRESS INFO</div>
  <div class="abs address">
    <div class="org">LEARNING UPLIFT COLLECTIVE FZC</div>
    Business Center<br>Al Noora Building<br>UAE Free Trade Zone, Ras Sahra,<br>UAE
  </div>
  <div class="contact-line" style="top:2642px"><svg width="16" height="16" viewBox="0 0 16 16"><path d="M4 1 L6.5 4.5 L5 6.5 Q6.5 9.5 9.5 11 L11.5 9.5 L15 12 L13 15 Q6 14 1 3 Z" fill="var(--dark)"/></svg>1-800-555-0142</div>
  <div class="contact-line" style="top:2672px"><svg width="16" height="16" viewBox="0 0 16 16"><rect x="1" y="3" width="14" height="10" fill="var(--dark)"/><path d="M1 3 L8 9 L15 3" fill="none" stroke="#fff" stroke-width="1.3"/></svg>info@learnuplift.com</div>
  <div class="contact-line" style="top:2703px"><svg width="16" height="16" viewBox="0 0 16 16"><path d="M8 1 A5 5 0 0 1 13 6 Q13 9 8 15 Q3 9 3 6 A5 5 0 0 1 8 1 Z" fill="var(--dark)"/><circle cx="8" cy="6" r="2" fill="#fff"/></svg>Map Location</div>

  <div class="abs footer-head" style="left:415px;top:2487px">QUICK CONTACT</div>
  <div class="field" style="left:415px;top:2529px;width:199px">Name</div>
  <div class="field" style="left:628px;top:2529px;width:201px">Email Address</div>
  <div class="field" style="left:415px;top:2577px;width:199px">Phone No.</div>
  <div class="field field-select" style="left:628px;top:2577px;width:201px">Select Service</div>
  <div class="field" style="left:415px;top:2625px;width:414px;height:57px">Message</div>
  <a class="btn" style="left:724px;top:2696px;width:105px;height:38px">SEND</a>

  <div class="divider-v" style="left:858px;top:2477px;height:255px"></div>
  <div class="abs kicker" style="right:73px;top:2577px">GET IN TOUCH</div>
  <h2 class="abs section-title" style="right:73px;top:2603px;font-size:36px">CONTACT US</h2>
</section>

<footer class="bottom-bar">
  <div class="copyright">Copyright © 2017. Company Name. All Right Reserved</div>
  <div class="social" aria-label="Social media links"><span></span><span></span><span></span><span></span><span></span><span></span></div>
</footer>

</body>
</html>
```